Luxury startup skincare company needs packaging design

We want a label design for glass jars and a packaging box. The label design will be unique, clean, classy, and expensive looking. The design must be eye-catching and colorful, bold and universal. I

I've attached the logo variations for your reference. The glass jar will need a label for the top as well as a wrap-around label and the packaging will need to be designed per specs that will be provided. We currently have one product and will be expanding to several once the brand grows.

Target Market(s)

Women with disposable income 25-65 years old who care about their skincare routine

Industry/Entity Type

Beauty

Font styles to use
Decorative

Requirements
Must have
• my logo

```html
<!DOCTYPE html>
<html lang="en">
<head>
<meta charset="utf-8">
<title>Velour Crest Repairing Mask Label</title>
<link rel="stylesheet" href="https://fonts.googleapis.com/css2?family=Playfair+Display:wght@700&family=Raleway:wght@300;400;700&display=swap">
<style>
  :root {
    --page: #f4f2f1;
    --label: #141414;
    --ink-light: #f2f0ef;
    --rose: #b98680;
    --rose-light: #dcb0a8;
    --rose-dark: #8f5f5a;
    --panel-white: #ffffff;
  }
  * { margin: 0; padding: 0; box-sizing: border-box; }
  html, body { width: 1164px; height: 1200px; overflow: hidden; background: var(--page); }
  .label {
    position: absolute; left: 30px; top: 240px; width: 1104px; height: 720px;
    background: var(--label); color: var(--ink-light);
    font-family: "Raleway", sans-serif; overflow: hidden;
  }
  .side-copy {
    position: absolute; font-size: 14.5px; line-height: 21px; font-weight: 400;
  }
  .side-copy p + p { margin-top: 24px; }
  .side-copy--left { left: 44px; top: 70px; width: 290px; }
  .side-copy--right {
    left: 926px; top: 70px; width: 158px; text-align: right;
    font-size: 13px; line-height: 19px;
  }
  .side-copy--right p + p { margin-top: 20px; }
  .brand {
    position: absolute; left: 380px; top: 160px; width: 400px;
    font-weight: 300; color: var(--ink-light); letter-spacing: 18px;
  }
  .brand__name { font-size: 40px; line-height: 48px; }
  .brand__sub { font-size: 24px; line-height: 36px; letter-spacing: 20px; }
  .product-title {
    position: absolute; left: 360px; top: 300px; width: 440px; text-align: center;
    font-family: "Playfair Display", serif; font-weight: 700;
    font-size: 74px; line-height: 80px; color: var(--ink-light);
  }
  .claim {
    position: absolute; left: 375px; top: 490px; width: 420px; height: 54px;
    background: var(--rose); border-radius: 0 27px 27px 0;
    display: flex; align-items: center; justify-content: center;
    font-weight: 700; font-size: 22px; color: var(--label); letter-spacing: 0.3px;
  }
  .tagline {
    position: absolute; left: 360px; top: 565px; width: 440px; text-align: center;
    font-size: 21px; line-height: 28px; font-weight: 400;
  }
  .profile-art { position: absolute; left: 800px; top: 0; width: 120px; height: 720px; }
  .batch-panel {
    position: absolute; left: 954px; top: 490px; width: 130px; height: 170px;
    background: var(--panel-white);
  }
</style>
</head>
<body>
  <section class="label">
    <div class="side-copy side-copy--left">
      <p>Our rich treatment mask melts into every strand, softening dry ends and calming frizz. Argan oil and shea butter work together to seal in moisture, leaving curls and coils smooth, bouncy and full of natural shine every single day.</p>
      <p>Apply a generous amount to clean, damp hair from root to tip. Comb through gently with a wide tooth comb and leave on for ten to fifteen minutes. Rinse well with cool water for best results and lasting softness.</p>
      <p>For external use only. Avoid direct contact with eyes. If irritation occurs, stop use and rinse well. Store in a cool, dry place away from direct sunlight. Keep the lid closed tightly after each use. Keep out of reach of children.</p>
    </div>

    <div class="brand">
      <div class="brand__name">VELOUR</div>
      <div class="brand__sub">CREST</div>
    </div>

    <h1 class="product-title">REPAIRING<br>MASK</h1>
    <div class="claim">INFUSED WITH ARGAN OIL</div>
    <p class="tagline">Deep moisturization to replenish<br>and help restore hair health</p>

    <svg class="profile-art" viewBox="0 0 120 720" role="img" aria-label="Rose-toned profile silhouette illustration of a woman">
      <defs>
        <linearGradient id="roseFade" x1="0" y1="0" x2="0" y2="1">
          <stop offset="0" stop-color="#8f5f5a"/>
          <stop offset="1" stop-color="#dcb0a8"/>
        </linearGradient>
      </defs>
      <path d="M50 0 C108 120 116 320 86 470 C62 580 16 620 8 720 L48 720 C56 640 102 570 114 450 C118 300 102 120 72 0 Z" fill="url(#roseFade)"/>
    </svg>

    <div class="side-copy side-copy--right">
      <p>Made for every texture, this mask restores strength to weak, brittle hair and helps prevent breakage. Free from sulfates, parabens and mineral oil.</p>
      <p>Ingredients: aqua, butyrospermum parkii butter, argania spinosa kernel oil, cetearyl alcohol, glycerin, panthenol, tocopherol, parfum, citric acid.</p>
    </div>

    <div class="batch-panel"></div>
  </section>
</body>
</html>
```